Lantern Forge needs a business card

The logo we have uploaded is going to be the image centered on the back.
The business card color is going to be black. Increase the contrast in the logo and lettering so the grey stands out from the black and is more readable. Keep the shadow effect if you can.
On the front, the only part of the logo that should be used is the Egyptian character. We would like the following information included: Name (first last), Title, Phone number, email and company name (Lantern Forge).
The images of colored sound waves we uploaded is a concept we would like implemented on the front as well but please do not use the exact image. It is for guideline purposes.
Get creative with the empty space. We are a technology company that deals with sound and lights. Please not too busy.
Thank you, we look forward to all your submissions.

```html
<!DOCTYPE html>
<html lang="en">
<head>
<meta charset="utf-8">
<title>Lantern Forge Business Card</title>
<link rel="stylesheet" href="https://fonts.googleapis.com/css2?family=Open+Sans:wght@400;600;700&display=swap">
<style>
  :root {
    --backdrop: #e9e6e1;
    --card-black: #1b1b1d;
    --card-black-soft: #262628;
    --card-white: #ffffff;
    --brand-red: #e2343b;
    --brand-grey: #8a8a8c;
    --ink: #1d1d1f;
    --ink-soft: #3a3a3c;
  }
  * { box-sizing: border-box; margin: 0; padding: 0; }
  html, body {
    width: 1200px;
    height: 892px;
    overflow: hidden;
    background: var(--backdrop);
    font-family: "Open Sans", Arial, sans-serif;
  }
  .canvas {
    position: relative;
    width: 1200px;
    height: 892px;
  }
  .card {
    position: absolute;
    width: 700px;
    height: 400px;
    border-radius: 4px;
    overflow: hidden;
    box-shadow: 0 10px 28px rgba(0,0,0,0.28);
  }
  .card-back {
    left: 440px;
    top: 60px;
    background: linear-gradient(160deg, var(--card-black-soft), var(--card-black));
    display: flex;
    align-items: center;
    justify-content: center;
  }
  .card-front {
    left: 70px;
    top: 430px;
    background: var(--card-white);
  }
  .front-header {
    position: absolute;
    left: 0; top: 0;
    width: 100%;
    height: 160px;
    background: linear-gradient(160deg, var(--card-black-soft), var(--card-black));
    display: flex;
    align-items: center;
    justify-content: center;
  }
  .front-rule {
    position: absolute;
    left: 0;
    top: 168px;
    width: 100%;
    height: 4px;
    background: var(--card-black);
  }
  .brand {
    display: flex;
    align-items: center;
    gap: 14px;
  }
  .brand-mark {
    background: var(--brand-grey);
  }
  .brand-name {
    color: var(--brand-red);
    font-weight: 600;
    letter-spacing: 0.12em;
    text-transform: uppercase;
  }
  .card-back .brand-mark { width: 30px; height: 30px; }
  .card-back .brand-name { font-size: 38px; }
  .front-header .brand-mark { width: 20px; height: 20px; }
  .front-header .brand-name { font-size: 26px; }
  .contact {
    position: absolute;
    left: 96px;
    top: 200px;
  }
  .contact-name {
    color: var(--brand-red);
    font-size: 34px;
    font-weight: 700;
    line-height: 1.1;
  }
  .contact-title {
    color: var(--ink-soft);
    font-size: 17px;
    margin: 2px 0 12px 40px;
  }
  .contact-line {
    color: var(--ink);
    font-size: 19px;
    line-height: 1.5;
  }
</style>
</head>
<body>
<main class="canvas">
  <section class="card card-back" aria-label="Card back">
    <div class="brand">
      <span class="brand-mark"></span>
      <span class="brand-name">Lantern Forge</span>
    </div>
  </section>

  <section class="card card-front" aria-label="Card front">
    <div class="front-header">
      <div class="brand">
        <span class="brand-mark"></span>
        <span class="brand-name">Lantern Forge</span>
      </div>
    </div>
    <div class="front-rule"></div>
    <div class="contact">
      <p class="contact-name">Employee Name</p>
      <p class="contact-title">Managing Director</p>
      <p class="contact-line">Phone : 036-7215 3908</p>
      <p class="contact-line">Web : www.website.com</p>
      <p class="contact-line">Email : info@website.com</p>
    </div>
  </section>
</main>
</body>
</html>
```